New Update: I am changing the title of the book and the back cover text. Title was too long before. Same style as before.
New Title: Standing Again
New Subtitle: One Family’s Road Back to Wholeness (italics on front cover)

Back cover text:
Standing Again: One Family’s Road Back to Wholeness offers clear, compassionate guidance for those recovering from total loss. Drawing from his experience as a Carrow Storm survivor, Tobias Lindqvell shares practical advice on insurance, rebuilding, and emotional healing, along with lessons in strength and community. This is not a book about tragedy; it’s about perseverance and renewal. Standing Again is a trusted companion for anyone rebuilding life, home, and hope after disaster.

Font styles to use
Serif

Colors
EB3D1F
EC4F4E
F09395
F8D3D4
FCEDEE

Requirements
Should not have
• No pictures or anything related to fire on the cover.

```html
<!DOCTYPE html>
<html lang="en">
<head>
<meta charset="utf-8">
<title>Standing Again – Cover Options</title>
<link href="https://fonts.googleapis.com/css2?family=Abril+Fatface&family=Playfair+Display:ital,wght@0,700;0,900;1,800&display=swap" rel="stylesheet">
<style>
  :root{
    --page:#ffffff;
    --ink:#000000;
    --text:#ffffff;
    --red-hot:#EB3D1F;
    --red-warm:#EC4F4E;
    --red-deep:#6e1410;
    --red-dark:#2a0705;
    --red-night:#120201;
    --photo-a:#e7e6e4;
    --photo-b:#2b3550;
  }
  *{box-sizing:border-box;margin:0;padding:0}
  html,body{width:1200px;height:1200px;overflow:hidden;background:var(--page)}
  .sheet{position:relative;width:1200px;height:1200px}
  .option-number{
    position:absolute;font-family:"Abril Fatface",serif;color:var(--ink);
    font-size:196px;line-height:1;
  }
  .option-number.one{left:152px;top:214px}
  .option-number.two{left:155px;top:805px}
  .cover{
    position:absolute;left:381px;width:777px;height:559px;overflow:hidden;
    background:
      radial-gradient(ellipse 260px 130px at 20px 30px, rgba(240,90,60,.95), transparent 70%),
      radial-gradient(ellipse 180px 220px at 790px 0px, rgba(210,45,40,.9), transparent 70%),
      linear-gradient(155deg, transparent 30%, rgba(120,20,15,.7) 45%, transparent 58%),
      linear-gradient(200deg, transparent 55%, rgba(110,18,14,.6) 66%, transparent 78%),
      radial-gradient(ellipse 300px 120px at 620px 560px, var(--red-night), transparent 80%),
      linear-gradient(135deg, #b2301f 0%, var(--red-deep) 25%, var(--red-dark) 45%, #5a0f0c 65%, #3a0806 85%, var(--red-night) 100%);
  }
  .cover.first{top:41px}
  .cover.second{top:621px}
  .blurb{
    position:absolute;left:54px;width:272px;
    font-family:Arial,Helvetica,sans-serif;font-weight:700;color:var(--text);
    font-size:11.6px;line-height:14.2px;
  }
  .blurb p+p{margin-top:6px}
  .first .blurb{top:111px}
  .second .blurb{top:153px}
  .divider{position:absolute;left:125px;width:127px;height:2px;background:var(--text)}
  .first .divider{top:300px}
  .second .divider{top:321px}
  .author-photo{position:absolute;left:150px;width:78px;height:80px;border:1px solid var(--text)}
  .first .author-photo{top:331px}
  .second .author-photo{top:332px}
  .photo-caption{
    position:absolute;left:120px;width:138px;text-align:center;
    font-family:"Playfair Display",serif;font-weight:900;font-size:9px;color:var(--text);
  }
  .first .photo-caption{top:417px}
  .second .photo-caption{top:418px}
  .code-box{position:absolute;left:223px;width:107px;height:57px;background:var(--text)}
  .first .code-box{top:464px}
  .second .code-box{top:466px}
  .spine-text{
    position:absolute;left:382px;writing-mode:vertical-rl;
    font-family:"Playfair Display",serif;font-weight:900;font-size:10px;color:var(--text);
    letter-spacing:.2px;
  }
  .spine-title{top:176px}
  .spine-author{top:303px}
  .front{position:absolute;left:404px;width:373px;text-align:center;color:var(--text)}
  .front-title{font-family:"Abril Fatface",serif;font-weight:400;text-transform:uppercase}
  .first .front-title{margin-top:92px;font-size:52px;line-height:60px}
  .second .front-title{margin-top:180px;font-size:56px;line-height:52px}
  .front-subtitle{font-family:"Playfair Display",serif;font-style:italic;font-weight:800;font-size:22px;line-height:30px}
  .first .front-subtitle{margin-top:38px}
  .second .front-subtitle{margin-top:12px}
  .front-author{position:absolute;left:0;width:100%;font-family:"Playfair Display",serif;font-weight:900;text-transform:uppercase}
  .first .front-author{top:484px;font-size:24px}
  .second .front-author{top:488px;font-size:20px}
</style>
</head>
<body>
<div class="sheet">
  <div class="option-number one">1</div>
  <div class="option-number two">2</div>

  <section class="cover first">
    <div class="blurb">
      <p>Standing Again: One Family’s Road Back to Wholeness offers clear, compassionate guidance for those recovering from total loss. Drawing from his experience as a Carrow Storm survivor, Tobias Lindqvell shares practical advice on insurance, rebuilding, and emotional healing, along with lessons in strength and community.</p>
      <p>This is not a book about tragedy; it’s about perseverance and renewal. Standing Again is a trusted companion for anyone rebuilding life, home, and hope after disaster.</p>
    </div>
    <div class="divider"></div>
    <svg class="author-photo" role="img" aria-label="Author portrait photograph" viewBox="0 0 78 80" preserveAspectRatio="none">
      <defs><linearGradient id="p1" x1="0" y1="0" x2="0" y2="1"><stop offset="0" stop-color="#e7e6e4"/><stop offset=".55" stop-color="#cfcac6"/><stop offset="1" stop-color="#2b3550"/></linearGradient></defs>
      <rect width="78" height="80" fill="url(#p1)"/>
    </svg>
    <div class="photo-caption">TOBIAS LINDQVELL</div>
    <div class="code-box"></div>
    <div class="spine-text spine-title">STANDING AGAIN</div>
    <div class="spine-text spine-author">TOBIAS LINDQVELL</div>
    <div class="front">
      <h1 class="front-title">Standing<br>Again</h1>
      <p class="front-subtitle">One Family’s Road Back<br>to Wholeness</p>
    </div>
    <div class="front" style="top:0;height:559px"><div class="front-author">Tobias Lindqvell</div></div>
  </section>

  <section class="cover second">
    <div class="blurb">
      <p>Standing Again: One Family’s Road Back to Wholeness offers clear, compassionate guidance for those recovering from total loss. Drawing from his experience as a Carrow Storm survivor, Tobias Lindqvell shares practical advice on insurance, rebuilding, and emotional healing, along with lessons in strength and community.</p>
      <p>This is not a book about tragedy; it’s about perseverance and renewal. Standing Again is a trusted companion for anyone rebuilding life, home, and hope after disaster.</p>
    </div>
    <div class="divider"></div>
    <svg class="author-photo" role="img" aria-label="Author portrait photograph" viewBox="0 0 78 80" preserveAspectRatio="none">
      <defs><linearGradient id="p2" x1="0" y1="0" x2="0" y2="1"><stop offset="0" stop-color="#e7e6e4"/><stop offset=".55" stop-color="#cfcac6"/><stop offset="1" stop-color="#2b3550"/></linearGradient></defs>
      <rect width="78" height="80" fill="url(#p2)"/>
    </svg>
    <div class="photo-caption">TOBIAS LINDQVELL</div>
    <div class="code-box"></div>
    <div class="spine-text spine-title">STANDING AGAIN</div>
    <div class="spine-text spine-author">TOBIAS LINDQVELL</div>
    <div class="front">
      <h1 class="front-title">Standing<br>Again</h1>
      <p class="front-subtitle">One Family’s Road Back<br>to Wholeness</p>
    </div>
    <div class="front" style="top:0;height:559px"><div class="front-author">Tobias Lindqvell</div></div>
  </section>
</div>
</body>
</html>
```